Web design for online activity booking website

Our activity booking website uTrundle.net is looking outdated and needing a loving revamp on its design and STRUCTURE. it was initially created as a destination guide before we modified the homepage slightly to sell activities. So please DON'T RELY on the current website for your design. Now, the focus is ACTIVITY, while guide/ info should come only as secondary.

In other words, we will be doing something very similar to Plomaro.com (a bit crowded for our liking) and FindMyTrailpal.com. If you could capture the best essences of both, that would be awesome! Besides, we also like nestlo.com's simplicity.

SIMPLE, CLEAN, BRIGHT, USER and MOBILE FRIENDLY please :)

We have a new logo created and some wireframes (a few more in progress) so you know the basic components required in each page. These are just rough ideas so please ignore the ratio/size, colours etc and if you have a better way of arranging or simplifying things, please do so :)

Help us make it a website that everyone would love!

Thank you in advance for your time and artistry.

Target Market(s)

Internet savvy travellers between 18-65

Industry/Entity Type

Tourism

Number of Pages Required

5+ page

Requirements
Must have
• SIMPLE, CLEAN feel, USER and MOBILE FRIENDLY please :)
• See attachments for rough structure. Will also need standard pages such as:
• - About Us
• - Contact Us
• - Wishlist etc
• Message from our developer "designer to keep layers in PSD format accurately so html/css code does not need to lead a mess in photoshop"
Nice to have
• UPDATE: We are so thrilled to receive so many web designs but on the other hand, the submissions are getting too generic and everyone's designs is almost looking identical (many look like they are “borrowed” from existing popular websites). This is making the selection and decision process very difficult.
• So instead of sending us more of the very similar homepage design with minor tweaks (which we can do during handover section anyway), please send us a design of more specific page of our website. Please refer job brief, file no. 5 - Product detail page.
• This will give us better idea of your skills and choose the best as winner to work on the rest of our web pages.
Should not have
• No dark background please

```html
<!DOCTYPE html>
<html lang="en">
<head>
<meta charset="utf-8">
<title>Kite Surf Group Lesson – uTrundle</title>
<link href="https://fonts.googleapis.com/css2?family=Roboto:ital,wght@0,300;0,400;0,500;0,700;1,400&family=Roboto+Condensed:wght@400;700&display=swap" rel="stylesheet">
<style>
:root{
  --purple-dark:#3b1856;
  --purple:#5a2a7c;
  --purple-accent:#6b2f92;
  --pink-btn:#a548c4;
  --slate:#2e4852;
  --ink:#333;
  --text:#666;
  --muted:#999;
  --line:#e2e2e2;
  --btn-dark:#3a3a3a;
  --star:#e5262b;
  --date:#3b6bd2;
  --foot-1:#f1f2f4;
  --foot-2:#e4e9ee;
}
*{box-sizing:border-box;margin:0;padding:0}
html,body{width:1200px;height:3629px;overflow:hidden;background:#fff}
body{font-family:"Roboto",Arial,sans-serif;color:var(--text);font-size:12px;position:relative}
ul{list-style:none}
a{color:inherit;text-decoration:none}

/* top bar + header */
.topbar{height:26px;background:var(--purple-dark);color:#fff;font-size:11px;display:flex;justify-content:space-between;align-items:center;padding:0 92px}
.topbar span{margin-right:18px}
.topbar .right span{margin:0 0 0 22px}
.header{height:95px;background:var(--purple);display:flex;align-items:center;padding:0 92px;position:relative}
.logo{font-family:"Roboto",sans-serif;font-weight:700;color:#fff;font-size:40px;letter-spacing:-1px;display:flex;align-items:center;gap:10px}
.logo i{width:14px;height:14px;border-radius:50%;background:#fff;display:block}
.search{position:absolute;left:428px;top:32px;display:flex;gap:14px}
.select{height:31px;background:#fff;border:1px solid #ccc;font-size:11px;color:#555;display:flex;align-items:center;justify-content:space-between;padding:0 10px}
.search .select{width:273px}
.go{height:31px;width:87px;background:var(--pink-btn);color:#fff;font-weight:700;font-size:12px;display:flex;align-items:center;justify-content:center}

/* layout */
.page{position:absolute;left:92px;top:145px;width:1016px;display:flex;justify-content:space-between}
.main{width:748px}
.side{width:250px}

/* product */
.product{display:flex;height:363px}
.product-photo{width:392px;height:303px;background:linear-gradient(160deg,#5fb9d8,#2c7ea6 55%,#d9eef4);}
.product-info{margin-left:18px;width:338px}
.product-info h1{font-family:"Roboto Condensed",sans-serif;font-size:21px;color:#222;letter-spacing:.5px}
.days{font-family:"Roboto Condensed",sans-serif;font-weight:700;font-size:14px;color:#555;margin:2px 0 10px}
.product-info p{font-size:12px;line-height:1.55;color:#666;height:100px}
.rating{border-top:1px solid var(--line);border-bottom:1px solid var(--line);padding:10px 0;display:flex;gap:10px;align-items:center;font-size:11px}
.stars{color:var(--star);letter-spacing:1px;font-size:13px}
.price-row{display:flex;justify-content:space-between;align-items:flex-end;margin-top:24px}
.from{font-size:10px;color:#999}
.price{font-size:36px;color:#444;font-weight:500}
.price small{font-size:16px;color:#777}
.btn-dark{background:var(--btn-dark);color:#fff;display:inline-flex;align-items:center;justify-content:center;gap:8px}
.book{width:168px;height:44px;font-size:17px}

.share{display:flex;align-items:center;gap:8px;height:44px}
.share h3{font-size:19px;font-weight:500;color:#444;margin-right:6px}
.share .c{width:32px;height:32px;border-radius:50%;background:#8a8f96;display:flex;align-items:center;justify-content:center}

.tabs{margin-top:0;height:40px;background:var(--btn-dark);display:flex;font-size:13px;color:#fff;margin-top:0}
.tabs li{flex:1;display:flex;align-items:center;justify-content:center;border-right:1px solid #555}
.tabs li.on{background:#fff;color:#333;border:1px solid #ccc;border-bottom:none}

.sect{margin-top:24px}
.sect h2{font-size:18px;font-weight:400;color:#555;border-bottom:1px solid var(--line);padding-bottom:10px;margin-bottom:16px}
.sect p{font-size:11.5px;line-height:1.75;color:#777;margin-bottom:18px}
.sublist{padding-left:8px}
.sublist h4{font-size:12px;color:#333;margin:6px 0 10px}
.sublist li{font-size:11.5px;color:#777;padding:0 0 11px 28px;position:relative}
.sublist li:before{content:"›";position:absolute;left:10px;top:-3px;font-size:15px;color:#555}
.sublist ul{border-bottom:1px solid #eee;margin-bottom:8px}
.map{height:232px;background:linear-gradient(135deg,#efe9d9,#e3dfd3 50%,#d5e3c9);border:1px solid #ddd}

/* reviews panel */
.reviews{margin-top:84px;margin-left:-7px;width:755px;height:774px;border:1px solid #e6e6e6;position:relative}
.reviews-head{height:50px;background:var(--btn-dark);color:#fff;display:flex;align-items:center;justify-content:space-between;padding:0 14px}
.reviews-head h2{font-size:20px;font-weight:400}
.reviews-head h2 small{font-size:12px}
.filter{display:flex;align-items:center;gap:8px;font-size:11px}
.filter .select{width:160px;height:24px;font-size:9px}
.review{height:160px;padding:18px 14px 0;border-bottom:1px solid #eee;position:relative}
.review h3{font-family:"Roboto Condensed",sans-serif;font-size:23px;color:#333;font-weight:700}
.review .stars{font-size:19px}
.review p{font-size:14px;color:#555;margin:10px 0 4px}
.review .by{font-size:11px;color:#888}
.review .name{font-size:11px;color:var(--purple-accent);font-style:italic;font-weight:500}
.review .date{position:absolute;right:20px;top:24px;color:var(--date);font-size:12px}
.helpful{position:absolute;right:20px;bottom:22px;font-size:11px;display:flex;align-items:center;gap:10px}
.yes{background:var(--purple);color:#fff;padding:3px 10px;font-size:11px}
.more-reviews{position:absolute;left:50%;transform:translateX(-50%);bottom:22px;width:210px;height:38px;font-size:14px}

/* sidebar */
.panel-head{height:50px;background:var(--slate);color:#fff;font-size:20px;display:flex;align-items:center;justify-content:center}
.panel-head.notch{clip-path:polygon(0 0,100% 0,100% 78%,50% 100%,0 78%);height:56px}
.booking{border:1px solid #ddd;height:392px}
.booking-body{padding:10px 14px;font-size:11px;color:#444}
.booking-body .small-sel{display:inline-flex;height:22px;border:1px solid #ccc;padding:0 6px;align-items:center;gap:10px;font-size:10px;margin-right:4px}
.booking-body .row{display:flex;align-items:center;justify-content:space-between;margin-bottom:10px}
.guarantee{color:var(--purple-accent);font-weight:700;font-size:10px;margin:6px 0 14px}
.hr{border-top:1px solid #ddd;margin:6px 0 10px}
.link{color:var(--purple-accent);font-size:10px}
.check{margin:16px auto 0;width:200px;height:40px;font-size:14px;display:flex}
.side-reviews{margin-top:14px;border:1px solid #ddd;height:766px}
.sr{margin:0 14px;padding:26px 0 14px;border-bottom:1px solid #ddd}
.sr h3{font-family:"Roboto Condensed",sans-serif;font-size:22px;color:#333}
.sr .stars{font-size:17px}
.sr p{font-size:11.5px;color:#666;margin:8px 0}
.sr small{font-size:9.5px;color:#555;display:block;line-height:1.4}
.sr small b{color:var(--purple-accent);font-style:italic;font-weight:500}
.sr small em{color:var(--date);font-style:italic}
.all-reviews{margin:22px auto 0;width:190px;height:38px;font-size:14px;display:flex}
.offer{margin-top:18px;height:224px;border-bottom:1px solid #eee}
.offer-img{height:128px;background:linear-gradient(180deg,#7ea9c9,#4c7a5c 55%,#6b4a33);position:relative}
.heart{position:absolute;right:0;top:0;width:34px;height:34px;background:var(--purple-accent);display:flex;align-items:center;justify-content:center}
.offer h4{font-size:11.5px;font-weight:400;color:#444;margin:8px 0 6px;line-height:1.35}
.offer .meta{display:flex;justify-content:space-between;align-items:flex-end}
.offer .stars{font-size:15px}
.offer .cnt{font-size:10px;color:#888}
.offer .p{text-align:right;color:#999;font-size:10px}
.offer .p b{font-size:20px;color:#444;font-weight:500}
.more-offer{margin:28px auto 0;width:200px;height:38px;font-size:14px;display:flex}

/* footers */
.foot-top{position:absolute;top:2992px;left:0;width:1200px;height:334px;background:var(--foot-1);padding:28px 92px 0;display:flex}
.foot-top .col{width:356px}
.foot-top h5{font-size:16px;font-weight:500;color:#444;margin-bottom:24px}
.foot-top li{font-size:11px;color:#555;padding:0 0 13px 22px;position:relative}
.foot-top li:before{content:"›";position:absolute;left:2px;top:-3px;font-size:14px}
.foot-bot{position:absolute;top:3326px;left:0;width:1200px;height:254px;background:var(--foot-2);padding:36px 92px 0;display:flex}
.foot-bot h5{font-size:12px;color:#333;font-weight:700;margin-bottom:14px}
.foot-bot li{font-size:11px;color:#555;margin-bottom:6px}
.fc1{width:253px}.fc2{width:235px}.fc3{width:228px}.fc4{width:290px}
.socials{display:flex;gap:24px;margin:8px 0 30px}
.socials i{width:20px;height:20px;background:#444;display:block}
.news{display:flex;margin-top:4px}
.news .in{width:190px;height:28px;background:#fff;border:1px solid #ccc;font-size:10px;color:#aaa;padding:0 8px;display:flex;align-items:center}
.news .btn-dark{width:78px;height:28px;font-size:11px}
.copy{position:absolute;top:3580px;left:0;width:1200px;height:49px;background:var(--purple-dark);color:#ddd;font-size:11px;display:flex;align-items:center;justify-content:center}
</style>
</head>
<body>

<div class="topbar">
  <div><span>Language ▾</span><span>Currency ▾</span></div>
  <div class="right"><span>✚ Help</span><span>♥ Favourite</span><span>● Log in</span></div>
</div>
<header class="header">
  <div class="logo"><i></i>uTrundle</div>
  <div class="search">
    <div class="select">Choose a destination <span>▾</span></div>
    <div class="select">Choose an activity <span>▾</span></div>
    <div class="go">LET'S GO!</div>
  </div>
</header>

<div class="page">
  <main class="main">
    <section class="product">
      <div class="product-photo" role="img" aria-label="Kite surfer riding a board across breaking ocean waves"></div>
      <div class="product-info">
        <h1>KITE SURF GROUP LESSON</h1>
        <div class="days">3 DAYS</div>
        <p>Sure, everyone knows about the coffee shops – but what else is fun to do in Amsterdam? Holland's capital city is a hub for happy cyclists, lazy boers by the canal, and art-lovers. As you start planning what to see, here are ten activities you can't miss! [...]</p>
        <div class="rating"><span class="stars">★★★★★</span><span>1475 Reviews</span></div>
        <div class="price-row">
          <div><div class="from">from US</div><div class="price"><small>$</small>654.00</div></div>
          <a class="btn-dark book">Book Now ›</a>
        </div>
      </div>
    </section>

    <div class="share">
      <h3>Share On:</h3>
      <span class="c"></span><span class="c"></span><span class="c"></span><span class="c"></span>
      <span class="c" style="background:#3aa657"><svg width="14" height="14" viewBox="0 0 14 14" fill="#fff"><circle cx="3" cy="7" r="2"/><circle cx="11" cy="3" r="2"/><circle cx="11" cy="11" r="2"/><path d="M3 7L11 3M3 7L11 11" stroke="#fff" stroke-width="1.3"/></svg></span>
      <span class="c" style="background:#f0902a"><svg width="14" height="14" viewBox="0 0 14 14" fill="#fff"><circle cx="3" cy="11" r="1.8"/><path d="M2 6a6 6 0 016 6M2 2a10 10 0 0110 10" stroke="#fff" stroke-width="1.8" fill="none"/></svg></span>
      <span class="c" style="background:#9aa0a6"><svg width="16" height="12" viewBox="0 0 16 12"><rect x="1" y="1" width="14" height="10" fill="#fff"/><path d="M1 1l7 6 7-6" stroke="#9aa0a6" fill="none"/></svg></span>
    </div>

    <ul class="tabs">
      <li class="on">Description</li><li>What's Included &amp; Not</li><li>Important Notes</li><li>Others</li><li>Map</li>
    </ul>

    <section class="sect">
      <h2>Description</h2>
      <p>Lorem ipsum dolor sit amet, consectetur adipiscing elit. Donec dignissim enim id ante convallis, quis pretium enim molestie. Cras et arcu dolor. Maecenas non nisl, ultrices ac posuere nec, euismod id lacus. Ut dictum hendrerit eleifend. Morbi mi tellus, feugiat fringilla feugiat porta, molestie eu neque.</p>
      <p>Phasellus sit amet orci quis massa gravida mollis ut mollis nibh. Sed sit amet egestas est, a tincidunt sem. Nulla tincidunt elit libero, a semper velit gravida id. Sed faucibus lorem quis sapien mattis, et tempor justo pretium. Pellentesque porttitor bibendum maximus. Mauris vitae tellus quis augue aliquam maximus. Sed vel lorem a lorem blandit tincidunt vel at nunc. Lorem ipsum dolor sit amet, consectetur adipiscing elit. Donec dignissim enim id ante convallis, quis pretium enim molestie. Cras et arcu dolor. Maecenas non nisl, ultrices ac posuere nec, euismod id lacus. Ut dictum hendrerit eleifend. Morbi mi tellus, feugiat fringilla feugiat porta, molestie eu neque.</p>
      <p>Phasellus sit amet orci quis massa gravida mollis ut mollis nibh. Sed sit amet egestas est, a tincidunt sem. Nulla tincidunt elit libero, a semper velit gravida id. Sed faucibus lorem quis sapien mattis, et tempor justo pretium. Pellentesque porttitor bibendum maximus. Mauris vitae tellus quis augue aliquam maximus. Sed vel lorem a lorem blandit tincidunt vel at nunc.</p>
    </section>

    <section class="sect">
      <h2>What's Included &amp; Not</h2>
      <div class="sublist">
        <h4>Price includes :</h4>
        <ul><li>Lorem ipsum dolor sit amet, consectetur adipiscing elit.</li><li>Quisque non nisi sed erat lobortis feugiat vitae sed lacus.</li><li>Fusce non ante in nulla feugiat imperdiet in id sem.</li><li>In ultricies augue vel velit dictum, ac aliquam magna congue.</li></ul>
        <h4>Price does not included :</h4>
        <ul style="border:none"><li>Lorem ipsum dolor sit amet, consectetur adipiscing elit.</li><li>Quisque non nisi sed erat lobortis feugiat vitae sed lacus.</li><li>Fusce non ante in nulla feugiat imperdiet in id sem.</li></ul>
      </div>
    </section>

    <section class="sect">
      <h2>Important Notes</h2>
      <div class="sublist">
        <h4>Prerequisites :</h4>
        <ul><li>Lorem ipsum dolor sit amet, consectetur adipiscing elit.</li><li>Quisque non nisi sed erat lobortis feugiat vitae sed lacus.</li><li>Fusce non ante in nulla feugiat imperdiet in id sem.</li><li>In ultricies augue vel velit dictum, ac aliquam magna congue.</li></ul>
        <h4>Please bring :</h4>
        <ul style="border:none"><li>Lorem ipsum dolor sit amet, consectetur adipiscing elit.</li><li>Quisque non nisi sed erat lobortis feugiat vitae sed lacus.</li><li>Fusce non ante in nulla feugiat imperdiet in id sem.</li></ul>
      </div>
    </section>

    <section class="sect">
      <h2>Others</h2>
      <p>Lorem ipsum dolor sit amet, consectetur adipiscing elit. Quisque non nisi sed erat lobortis feugiat vitae sed lacus. Fusce non ante in nulla feugiat imperdiet in id sem.In ultricies augue vel velit dictum, ac aliquam magna congue.</p>
    </section>

    <section class="sect" style="margin-top:8px">
      <h2>Map</h2>
      <div class="map" role="img" aria-label="Street map of central Amsterdam showing the meeting point"></div>
    </section>

    <section class="reviews">
      <div class="reviews-head">
        <h2>What Other People Are Saying <small>(1465 reviews)</small></h2>
        <div class="filter">Filer By rating <div class="select">see all reviews <span>▾</span></div></div>
      </div>
      <article class="review"><h3>"GREAT TOUR"</h3><div class="stars">★★★★★</div><p>Good visit, nice art, good cafe.</p><div class="by">Reviewed By</div><div class="name">uTrundle Customer (United States)</div><div class="date">November 27, 2015</div><div class="helpful">was this helpful? <span class="yes">Yes</span></div></article>
      <article class="review"><h3>"GREAT TOUR"</h3><div class="stars">★★★★★</div><p>Good visit, nice art, good cafe.</p><div class="by">Reviewed By</div><div class="name">uTrundle Customer (United States)</div><div class="date">November 27, 2015</div><div class="helpful">was this helpful? <span class="yes">Yes</span></div></article>
      <article class="review"><h3>"GREAT TOUR"</h3><div class="stars">★★★★★</div><p>Good visit, nice art, good cafe.</p><div class="by">Reviewed By</div><div class="name">uTrundle Customer (United States)</div><div class="date">November 27, 2015</div><div class="helpful">was this helpful? <span class="yes">Yes</span></div></article>
      <article class="review" style="border:none"><h3>"GREAT TOUR"</h3><div class="stars">★★★★★</div><p>Good visit, nice art, good cafe.</p><div class="by">Reviewed By</div><div class="name">uTrundle Customer (United States)</div><div class="date">November 27, 2015</div><div class="helpful">was this helpful? <span class="yes">Yes</span></div></article>
      <a class="btn-dark more-reviews">Show More Review ›</a>
    </section>
  </main>

  <aside class="side">
    <div class="booking">
      <div class="panel-head">Booking Calendar</div>
      <div class="booking-body">
        <div style="margin:4px 0 8px">Select Travel Date</div>
        <div class="row" style="justify-content:flex-start"><span class="small-sel">02 ▾</span><span class="small-sel">Dec 2015 ▾</span>
          <svg width="16" height="16" viewBox="0 0 16 16" style="margin-left:auto"><rect x="1" y="3" width="14" height="12" fill="#555"/><rect x="3" y="7" width="10" height="6" fill="#fff"/><rect x="4" y="1" width="2" height="4" fill="#555"/><rect x="10" y="1" width="2" height="4" fill="#555"/></svg></div>
        <div class="guarantee">FLEXIBLE DATE GUARANTEE ›</div>
        <div class="hr"></div>
        <div style="margin-bottom:12px">Enter Total Number of Travellers</div>
        <div class="row"><span>Adult( Age 3+)</span><span class="small-sel" style="margin-right:30px">0 ▾</span></div>
        <div class="row"><span>Infant ( age 0 to 2)</span><span class="small-sel" style="margin-right:30px">0 ▾</span></div>
        <div class="link">What this, and can I change it?</div>
        <div class="hr" style="margin-top:14px"></div>
        <a class="btn-dark check">Check Availability ›</a>
      </div>
    </div>

    <div class="side-reviews">
      <div class="panel-head notch">Reviews</div>
      <div class="sr"><h3>"GREAT TOUR"</h3><div class="stars">★★★★★</div><p>Good visit, nice art, good cafe.</p><small>From <b>Noah Fielding(United States)</b> on <em>November 27, 2015</em></small></div>
      <div class="sr"><h3>"GREAT TOUR"</h3><div class="stars">★★★★★</div><p>Good visit, nice art, good cafe.</p><small>From <b>Noah Fielding(United States)</b> on <em>November 27, 2015</em></small></div>
      <div class="sr"><h3>"GREAT TOUR"</h3><div class="stars">★★★★★</div><p>Good visit, nice art, good cafe.</p><small>From <b>Noah Fielding(United States)</b> on <em>November 27, 2015</em></small></div>
      <div class="sr" style="padding-top:40px"><h3>"GREAT TOUR"</h3><div class="stars">★★★★★</div><p>Good visit, nice art, good cafe.</p><small>From <b>Noah Fielding(United States)</b> on <em>November 27, 2015</em></small></div>
      <a class="btn-dark all-reviews">See All Reviews ›</a>
    </div>

    <div class="offer"><div class="offer-img" role="img" aria-label="Wooden boathouse on a mountain lake"><span class="heart"><svg width="18" height="16" viewBox="0 0 18 16"><path d="M9 15L2 8a4 4 0 016-6l1 1 1-1a4 4 0 016 6z" fill="#fff"/></svg></span></div><h4>Amsterdam: 1.5-Hour Evening Canal Cruise</h4><div class="meta"><div><div class="stars">★★★★★</div><div class="cnt">1465 Review</div></div><div class="p">From<br><b>US$ 16</b></div></div></div>
    <div class="offer"><div class="offer-img" role="img" aria-label="Wooden boathouse on a mountain lake"><span class="heart"><svg width="18" height="16" viewBox="0 0 18 16"><path d="M9 15L2 8a4 4 0 016-6l1 1 1-1a4 4 0 016 6z" fill="#fff"/></svg></span></div><h4>Amsterdam: 1.5-Hour Evening Canal Cruise</h4><div class="meta"><div><div class="stars">★★★★★</div><div class="cnt">1465 Review</div></div><div class="p">From<br><b>US$ 16</b></div></div></div>
    <div class="offer"><div class="offer-img" role="img" aria-label="Wooden boathouse on a mountain lake"><span class="heart"><svg width="18" height="16" viewBox="0 0 18 16"><path d="M9 15L2 8a4 4 0 016-6l1 1 1-1a4 4 0 016 6z" fill="#fff"/></svg></span></div><h4>Amsterdam: 1.5-Hour Evening Canal Cruise</h4><div class="meta"><div><div class="stars">★★★★★</div><div class="cnt">1465 Review</div></div><div class="p">From<br><b>US$ 16</b></div></div></div>
    <div class="offer"><div class="offer-img" role="img" aria-label="Wooden boathouse on a mountain lake"><span class="heart"><svg width="18" height="16" viewBox="0 0 18 16"><path d="M9 15L2 8a4 4 0 016-6l1 1 1-1a4 4 0 016 6z" fill="#fff"/></svg></span></div><h4>Amsterdam: 1.5-Hour Evening Canal Cruise</h4><div class="meta"><div><div class="stars">★★★★★</div><div class="cnt">1465 Review</div></div><div class="p">From<br><b>US$ 16</b></div></div></div>
    <div class="offer"><div class="offer-img" role="img" aria-label="Wooden boathouse on a mountain lake"><span class="heart"><svg width="18" height="16" viewBox="0 0 18 16"><path d="M9 15L2 8a4 4 0 016-6l1 1 1-1a4 4 0 016 6z" fill="#fff"/></svg></span></div><h4>Amsterdam: 1.5-Hour Evening Canal Cruise</h4><div class="meta"><div><div class="stars">★★★★★</div><div class="cnt">1465 Review</div></div><div class="p">From<br><b>US$ 16</b></div></div></div>
    <a class="btn-dark more-offer">Show More Offer ›</a>
  </aside>
</div>

<footer>
  <div class="foot-top">
    <div class="col"><h5>TOP DESTINATIONS</h5><ul><li>San Juan: Tours &amp; Tickets online</li><li>Barcelona: Tours &amp; Tickets online</li><li>New York: Tours &amp; Tickets online</li><li>Reykjavik: Tours &amp; Tickets online</li><li>Amsterdam: Tours &amp; Tickets online</li><li>Zadar: Tours &amp; Tickets online</li><li>Jerusalem: Tours &amp; Tickets online</li><li>Sydney: Tours &amp; Tickets online</li></ul></div>
    <div class="col"><h5>POPULAR ON UTRUNDLE</h5><ul><li>Paris Dinner &amp; Lunch Cruises</li><li>Dubai Quad &amp; ATV Tours</li><li>Rome Hop-on Hop-off Tours</li><li>Rome Gyro Scooter Tours</li><li>London Wizard Trail Tours</li><li>Barcelona Gyro Scooter Tours</li><li>San Francisco Gyro Scooter Tours</li><li>Mykonos Sailing Trips &amp; Boat Tours</li></ul></div>
    <div class="col"><h5>POPULAR ATTRACTIONS</h5><ul><li>Iron Lattice Tower: Tours &amp; Tickets online</li><li>Film Studio Backlot London: Tours &amp; Tickets online</li><li>Alhambra: Tours &amp; Tickets online</li><li>Burj Khalifa: Tours &amp; Tickets online</li><li>Doge's Palace: Tours &amp; Tickets online</li><li>Hermitage Museum: Tours &amp; Tickets online</li><li>Colosseum: Tours &amp; Tickets online</li><li>Canal House Museum: Tours &amp; Tickets online</li></ul></div>
  </div>
  <div class="foot-bot">
    <div class="fc1"><h5>COMPANY</h5><ul><li>About uTrundle.net</li><li>corporate Info</li><li>Site map?</li><li>Blog</li><li>Careers</li></ul></div>
    <div class="fc2"><h5>SUPPORT</h5><ul><li>Contact Us</li><li>FAQs</li></ul><h5 style="margin-top:22px">T &amp; C</h5><ul><li>Privacy Policy</li><li>Legal</li></ul></div>
    <div class="fc3"><h5>PARTNERSHIPS</h5><ul><li>Supplier Sign-up</li><li>Affiliate Programs</li></ul><h5 style="margin-top:22px">LOG-INS</h5><ul><li>Customers</li><li>Suppliers</li></ul></div>
    <div class="fc4"><h5>BE SOCIALS</h5><div class="socials"><i></i><i></i><i></i><i></i><i></i><i></i></div><h5>SUBSCRIBE NEWSLETTERS</h5><div class="news"><div class="in">your email id</div><a class="btn-dark">Subscribe</a></div></div>
  </div>
  <div class="copy">© 2015, All Rights Reserved, uTrundle.net</div>
</footer>

</body>
</html>
```